Professional modern business card design

A business card for my nutrition business, wanting a professional look, with info clearly visible. Open to using logo colours too.

Would like key info on the front -
logo
my name and qualifications
email
phone number

and just an enlarged logo again / image on the back.

```html
<!DOCTYPE html>
<html lang="en">
<head>
<meta charset="utf-8">
<title>Rowan Nutrition – Business Card</title>
<link href="https://fonts.googleapis.com/css2?family=Oswald:wght@500&family=Poppins:wght@400;600&display=swap" rel="stylesheet">
<style>
  :root {
    --navy: #022a40;
    --lime: #d4e021;
    --white: #ffffff;
    --backdrop: #1c1c1e;
    --divider: #7d8c96;
  }
  * { box-sizing: border-box; margin: 0; padding: 0; }
  html, body {
    width: 1200px; height: 900px; overflow: hidden;
    background: var(--backdrop);
  }
  .canvas {
    width: 1200px; height: 900px;
    display: flex; flex-direction: column;
    align-items: center; justify-content: center; gap: 40px;
  }
  .card {
    position: relative;
    width: 640px; height: 366px;
    background: var(--navy);
    overflow: hidden;
  }
  .card__band {
    position: absolute; left: 0; right: 0; bottom: 0;
    background: var(--lime);
  }
  .card--brand .card__band { height: 12px; }
  .card--contact .card__band { height: 14px; }

  /* Brand side */
  .brand-name {
    position: absolute; inset: 0 0 12px 0;
    display: flex; align-items: center; justify-content: center;
    font-family: 'Poppins', sans-serif;
    font-weight: 600;
    font-size: 54px;
    color: var(--white);
    letter-spacing: 0.5px;
  }

  /* Contact side */
  .contact-row {
    position: absolute; left: 0; right: 0; top: 168px;
    display: flex; align-items: center;
  }
  .identity {
    width: 300px; text-align: right; padding-right: 18px;
  }
  .identity__name {
    font-family: 'Oswald', sans-serif;
    font-weight: 500;
    font-size: 36px; line-height: 1.05;
    color: var(--lime);
  }
  .identity__role {
    font-family: 'Poppins', sans-serif;
    font-size: 13.5px;
    color: var(--white);
    margin-top: 2px;
    white-space: nowrap;
  }
  .divider {
    width: 1px; height: 74px; background: var(--divider);
  }
  .details {
    padding-left: 14px;
    font-family: 'Poppins', sans-serif;
    font-size: 14px; color: var(--white);
    display: flex; flex-direction: column; gap: 6px;
  }
  .details__item { display: flex; align-items: center; gap: 8px; }
  .details__icon { width: 15px; height: 15px; flex: none; }
</style>
</head>
<body>
<main class="canvas">
  <section class="card card--brand" aria-label="Card front">
    <div class="brand-name">Rowan Nutrition</div>
    <div class="card__band"></div>
  </section>

  <section class="card card--contact" aria-label="Card back">
    <div class="contact-row">
      <div class="identity">
        <div class="identity__name">Harriet Lowe</div>
        <div class="identity__role">Specialist Rehabilitation Dietitian</div>
      </div>
      <div class="divider"></div>
      <div class="details">
        <div class="details__item">
          <svg class="details__icon" viewBox="0 0 24 24" aria-hidden="true">
            <path fill="#d4e021" d="M6.6 10.8a15.1 15.1 0 0 0 6.6 6.6l2.2-2.2a1 1 0 0 1 1-.25 11.4 11.4 0 0 0 3.6.57 1 1 0 0 1 1 1V20a1 1 0 0 1-1 1A17 17 0 0 1 3 4a1 1 0 0 1 1-1h3.5a1 1 0 0 1 1 1c0 1.25.2 2.45.57 3.57a1 1 0 0 1-.25 1z"/>
          </svg>
          <span>07700900123</span>
        </div>
        <div class="details__item">
          <svg class="details__icon" viewBox="0 0 24 24" aria-hidden="true">
            <rect x="2" y="5" width="20" height="14" fill="#d4e021"/>
            <path d="M2 5l10 8 10-8" fill="none" stroke="#022a40" stroke-width="1.8"/>
          </svg>
          <span>harriet@rowannutrition.co.uk</span>
        </div>
      </div>
    </div>
    <div class="card__band"></div>
  </section>
</main>
</body>
</html>
```